WE ARE REACHING OUT TO CONTRACTORS TO HAVE AN OPPORTUNITY TO PROVIDE PROPOSALS FOR THEIR PROJECTS.

WE ARE A WASHINGTON DC. METRO AREA PLUMBING, HEATING AND AIR CONDITIONING CONTRACTOR. WE WOULD LIKE TO PRESENT A POSTCARD THAT OFFERS A FRENDLY, CONVENIENT WAY TO PROVIDE PROPOSALS FOR THEIR UP COMMING PROJECTS. WE WOULD APPRECIATE THE OPPURTUNITY TO PROVIDE ESTIMATES FOR YOUR UP COMMING PROJECTS. IF REQUESTED, WE WILL PROVIDE SAME DAY WALK THRU'S AND PROPOSALS. GET A 2ND OPINION, WE ALL LOOK AT PROJECTS DIFFERENTLY. CUSTOM HOMES, SUB DIVISIONS, REMODELING, SEWER AND WATER INSTALLATIONS AND REPLACEMENTS, WELL AND SEPTIC INSTALLATIONS AND REPAIRS, MECHANICAL EQUIPTMENT CHANGE OUTS, PLUMBING SYSTEMS REPLACEMENTS AND REPAIRS. RESIDENTAL AND COMERICAL CONSTRUCTION.. " WE DO IT ALL" JUST GIVE US A CALL. " WE WILL BE THERE " I WOULD LIKE MY BUSINESS CARD ON THE FRONT WITH SOME MODIFICATIONS AND THE ABOVE DESCRIPTION ON THE BACK. " HIGHLIGHTING WE WOULD APPRICATE THE OPPORTUNITY TO WORK WITH YOU COMPANY " SAME DAY WALK THRU'S AND PROPOSALS. PLEASE ADDRESS THE TOP OF THE BACK IN BOLD PRINT. " ATTENTION ESTIMATING " EYE CATCHING COLORS PLEASE. THANK YOU, TOM SELWYN

```html
<!DOCTYPE html>
<html lang="en">
<head>
<meta charset="utf-8">
<title>K.M. Hollis Mechanical Services – Business Card</title>
<link href="https://fonts.googleapis.com/css2?family=Russo+One&family=Roboto:wght@400;500;700&display=swap" rel="stylesheet">
<style>
  :root {
    --red: #e8262b;
    --white: #ffffff;
    --ink: #2b2b2b;
    --backdrop: #e9e9e9;
  }
  * { margin: 0; padding: 0; box-sizing: border-box; }
  html, body { width: 1200px; height: 1000px; overflow: hidden; }
  body { background: var(--backdrop); position: relative; font-family: "Roboto", Arial, sans-serif; }

  .card { position: absolute; top: 283px; width: 461px; height: 357px; background: var(--white); overflow: hidden; }
  .card--front { left: 84px; }
  .card--back { left: 658px; }

  /* Front */
  .brand { position: absolute; top: 0; left: 0; width: 100%; height: 122px; text-align: center; }
  .brand__name { position: absolute; top: 30px; left: 0; width: 100%; display: flex; justify-content: center; align-items: center; gap: 10px;
    font-family: "Russo One", sans-serif; font-size: 32px; color: var(--red); letter-spacing: 1px; }
  .brand__mark { width: 14px; height: 14px; background: var(--red); }
  .brand__sub { position: absolute; top: 64px; left: 0; width: 100%; font-family: "Russo One", sans-serif; font-size: 15px; color: var(--ink); letter-spacing: 0.5px; }
  .brand__rule { position: absolute; top: 90px; left: 66px; width: 335px; height: 6px;
    background: radial-gradient(ellipse at center, rgba(0,0,0,0.55) 0%, rgba(0,0,0,0) 70%); }

  .front-panel { position: absolute; top: 122px; left: 0; width: 100%; height: 235px; background: var(--red); color: var(--white); }
  .name-tab { position: absolute; top: 37px; left: 0; width: 191px; height: 32px; background: var(--white);
    font-family: "Roboto", sans-serif; font-weight: 700; font-size: 19px; color: var(--red); padding: 5px 0 0 34px; }
  .name-tab__shadow { position: absolute; top: 72px; left: 20px; width: 160px; height: 5px;
    background: radial-gradient(ellipse at center, rgba(0,0,0,0.45) 0%, rgba(0,0,0,0) 70%); }
  .contact { position: absolute; left: 34px; top: 103px; }
  .contact__phone { font-weight: 700; font-size: 21px; letter-spacing: 0.5px; }
  .contact__email { font-weight: 500; font-size: 12.5px; margin-top: 1px; }
  .contact__address { font-weight: 500; font-size: 11.5px; line-height: 16px; margin-top: 24px; }

  .divider { position: absolute; left: 228px; top: 45px; width: 1px; height: 160px; background: rgba(255,255,255,0.7); }
  .years { position: absolute; left: 249px; top: 34px; }
  .years__title { font-size: 23px; font-weight: 400; letter-spacing: 0.5px; }
  .years__text { font-size: 9.5px; line-height: 12px; font-weight: 400; }
  .years__star { position: absolute; left: 113px; top: -2px; }
  .services { position: absolute; left: 249px; top: 106px; list-style: none; font-weight: 700; font-size: 16px; line-height: 23px; letter-spacing: 0.3px; }
  .chevrons { position: absolute; right: 0; }

  /* Back */
  .back-header { position: absolute; top: 0; left: 0; width: 280px; height: 70px; background: var(--red); }
  .back-header__title { position: absolute; left: 24px; top: 14px; font-family: "Russo One", sans-serif; line-height: 22px; }
  .back-header__line1 { color: var(--white); font-size: 22px; letter-spacing: 0.5px; }
  .back-header__line2 { color: var(--ink); font-size: 22px; letter-spacing: 0.5px; }
  .back-body { position: absolute; top: 76px; left: 18px; width: 225px; font-size: 10px; line-height: 12.4px; color: var(--red); }
  .back-body__lead { font-weight: 700; }
  .back-body__plain { color: var(--ink); }
  .back-slogan { margin-top: 7px; font-family: "Russo One", sans-serif; font-size: 15.5px; line-height: 20px; }
  .back-slogan__call { font-family: "Roboto", sans-serif; color: var(--ink); font-size: 15px; }
</style>
</head>
<body>

<section class="card card--front">
  <header class="brand">
    <div class="brand__name"><span class="brand__mark"></span>K.M. HOLLIS</div>
    <div class="brand__sub">MECHANICAL SERVICES</div>
    <div class="brand__rule"></div>
  </header>

  <div class="front-panel">
    <div class="name-tab">TOM SELWYN</div>
    <div class="name-tab__shadow"></div>
    <div class="contact">
      <div class="contact__phone">301-555-0147</div>
      <div class="contact__email">TSELWYN@HOLLISMECH.COM</div>
      <div class="contact__address">1180 ALDER GLEN ROAD<br>FAIRHAVEN, MD 21700</div>
    </div>

    <div class="divider"></div>
    <div class="years">
      <div class="years__title">36 YEARS</div>
      <svg class="years__star" width="16" height="16" viewBox="0 0 16 16">
        <polygon fill="#fff" points="8,0 9.5,6 16,8 9.5,10 8,16 6.5,10 0,8 6.5,6"/>
      </svg>
      <div class="years__text">RESIDENTIAL AND COMMERCIAL<br>CONSTRUCTION AND REMODELING</div>
    </div>
    <ul class="services">
      <li>HEATING</li>
      <li>PLUMBING</li>
      <li>GAS FITTING</li>
      <li>AIR CONDITIONING</li>
    </ul>
    <svg class="chevrons" style="top:106px" width="90" height="86" viewBox="0 0 90 86">
      <polygon fill="#fff" points="34,0 90,0 90,18 22,18"/>
      <polygon fill="#fff" points="0,41 12,32 90,32 90,50 12,50"/>
      <polygon fill="#fff" points="22,64 90,64 90,82 34,82"/>
    </svg>
  </div>
</section>

<section class="card card--back">
  <header class="back-header">
    <div class="back-header__title">
      <div class="back-header__line1">ATTENTION</div>
      <div class="back-header__line2">ESTIMATING</div>
    </div>
    <svg class="chevrons" style="top:8px" width="66" height="56" viewBox="0 0 66 56">
      <polygon fill="#fff" points="24,0 66,0 66,10 14,10"/>
      <polygon fill="#fff" points="0,27 10,21 66,21 66,33 10,33"/>
      <polygon fill="#fff" points="14,44 66,44 66,54 24,54"/>
    </svg>
  </header>

  <div class="back-body">
    <p><span class="back-body__lead">We would appreciate the opportunity to provide estimates for your upcoming projects.</span> If requested, <span class="back-body__lead">we will provide same day walk thru's and proposals.</span></p>
    <p class="back-body__plain">Get a 2nd opinion,<br>24 hour proposal upon request.</p>
    <p>Design/Build services,Residential and Commerical Construction, New Buildings, Restaurants, Build Outs, Custom Homes, Sub Divisions, Sewer &amp; Water and Well &amp; Septic Installations and Replacements, Mechanical and Plumbing Systems Repair and Replacements.</p>
    <div class="back-slogan">
      <div>“WE DO IT ALL”</div>
      <div class="back-slogan__call">JUST GIVE US A CALL.</div>
      <div>“WE WILL BE THERE”</div>
    </div>
  </div>
</section>

</body>
</html>
```